Lucid Haven - Need Stationary Design

We need a stationary pack for our new Care company based in the uk
Are corporate colours are Pink and purple
Please use attached logo
Target Market(s)
The Care Industry
Industry/Entity Type
It Company
Contact Information for Business Card
Moira Blythe
Director

```html
<!DOCTYPE html>
<html lang="en">
<head>
<meta charset="utf-8">
<title>Lucid Haven – Stationery</title>
<link href="https://fonts.googleapis.com/css2?family=Arimo:wght@400;700&display=swap" rel="stylesheet">
<style>
:root{
  --backdrop:#a5acb1;
  --paper:#ffffff;
  --lavender:#e9c9f9;
  --purple:#7b3fa0;
  --pink:#ec2f8c;
  --ink:#2b2b2b;
  --soft-pink:#f7cfe4;
  --soft-lilac:#e3d4ee;
  --shadow:3px 4px 6px rgba(0,0,0,.28);
}
*{box-sizing:border-box;margin:0;padding:0}
html,body{width:1200px;height:733px;overflow:hidden}
body{background:var(--backdrop);font-family:"Arimo",Arial,sans-serif;color:var(--ink);position:relative}
.sheet{position:absolute;background:var(--paper);box-shadow:var(--shadow);overflow:hidden}
.brand{position:absolute;font-weight:400;color:var(--purple);white-space:nowrap;letter-spacing:.3px}
.brand-dot{display:block;border-radius:50%;background:var(--pink);margin:0 auto 4px}
.brand-lockup{position:absolute;text-align:center}
.brand-lockup .brand{position:static}
.address{position:absolute;font-size:7px;line-height:8.6px;white-space:nowrap}
.contacts{position:absolute;list-style:none;font-size:7px;white-space:nowrap}
.contacts li{display:flex;align-items:center;gap:4px;height:10.6px}
.contacts svg{width:7px;height:7px;flex:none}
.leaf-art{position:absolute;background:radial-gradient(ellipse at 70% 70%,var(--soft-pink) 0%,var(--soft-lilac) 45%,rgba(255,255,255,0) 75%)}

/* Letterhead */
.letterhead{left:71px;top:26px;width:484px;height:682px}
.letterhead .brand-lockup{left:0;right:0;top:46px}
.letterhead .brand{font-size:23px}
.letterhead .address{left:21px;top:600px}
.letterhead .contacts{left:21px;top:627px}
.letterhead .leaf-art{left:312px;top:451px;width:172px;height:231px}

/* Business card front */
.card-front{left:597px;top:29px;width:211px;height:124px;background:var(--lavender)}
.card-front .person{position:absolute;right:12px;top:9px;font-size:9px}
.card-front .person span{display:block;font-size:6px;text-align:right;color:var(--purple);margin-top:1px}
.card-front .brand{left:20px;top:39px;font-size:17px}
.card-front .address{left:72px;top:64px;font-size:6.8px}
.card-front .contacts{left:72px;top:84px;font-size:7px}
.card-front .contacts li{height:10.5px}

/* Business card back */
.card-back{left:831px;top:29px;width:211px;height:124px}
.card-back .brand-lockup{left:0;right:0;top:40px}
.card-back .brand{font-size:21px}

/* Envelope front */
.env-front{left:586px;top:209px;width:540px;height:233px}
.env-front .brand{left:13px;top:39px;font-size:13px}
.env-front .address{left:21px;top:163px;font-size:5.6px;line-height:7.4px}
.env-front .contacts{left:21px;top:186px;font-size:5.8px}
.env-front .contacts li{height:9.2px}
.env-front .contacts svg{width:6px;height:6px}
.env-front .leaf-art{left:367px;top:0;width:173px;height:233px}

/* Envelope back */
.env-back{left:586px;top:470px;width:540px;height:235px}
.env-back .flap{position:absolute;left:0;top:0;width:540px;height:100px}
.env-back .seal{position:absolute;left:257px;top:44px;width:24px;height:24px;border-radius:50%;background:var(--pink)}
</style>
</head>
<body>

<svg width="0" height="0" style="position:absolute">
  <defs>
    <symbol id="icon-phone" viewBox="0 0 10 10"><rect width="10" height="10" rx="2" fill="#ec2f8c"/><rect x="3" y="2" width="4" height="6" rx="1" fill="none" stroke="#fff" stroke-width="1"/></symbol>
    <symbol id="icon-mail" viewBox="0 0 10 10"><rect width="10" height="10" rx="2" fill="#ec2f8c"/><rect x="2" y="3" width="6" height="4" fill="none" stroke="#fff" stroke-width=".9"/><path d="M2 3l3 2.3L8 3" fill="none" stroke="#fff" stroke-width=".9"/></symbol>
    <symbol id="icon-web" viewBox="0 0 10 10"><rect width="10" height="10" rx="2" fill="#ec2f8c"/><circle cx="5" cy="5" r="2.8" fill="none" stroke="#fff" stroke-width=".9"/><path d="M2.2 5h5.6" stroke="#fff" stroke-width=".8"/></symbol>
  </defs>
</svg>

<section class="sheet letterhead">
  <div class="brand-lockup">
    <span class="brand-dot" style="width:34px;height:34px"></span>
    <div class="brand">Lucid Haven</div>
  </div>
  <p class="address">Your Address line C-236<br>Your Contry | your state -12345</p>
  <ul class="contacts">
    <li><svg><use href="#icon-phone"/></svg>123-456-7890</li>
    <li><svg><use href="#icon-phone"/></svg>123-456-7890</li>
    <li><svg><use href="#icon-mail"/></svg>hello@lucidhaven.co.uk</li>
    <li><svg><use href="#icon-web"/></svg>www.lucidhaven.co.uk</li>
  </ul>
  <div class="leaf-art" role="img" aria-label="Faint pink and lilac tree-of-care decoration"></div>
</section>

<section class="sheet card-front">
  <p class="person">Your Name</p>
  <div class="brand">Lucid Haven</div>
  <p class="address">Your Address line C-236<br>Your Contry | your state -12345</p>
  <ul class="contacts">
    <li><svg><use href="#icon-phone"/></svg>123-456-7890</li>
    <li><svg><use href="#icon-mail"/></svg>hello@lucidhaven.co.uk</li>
    <li><svg><use href="#icon-web"/></svg>www.lucidhaven.co.uk</li>
  </ul>
</section>

<section class="sheet card-back">
  <div class="brand-lockup">
    <span class="brand-dot" style="width:26px;height:26px"></span>
    <div class="brand">Lucid Haven</div>
  </div>
</section>

<section class="sheet env-front">
  <div class="brand">Lucid Haven</div>
  <p class="address">Your Address line C-236<br>Your Contry | your state -12345</p>
  <ul class="contacts">
    <li><svg><use href="#icon-phone"/></svg>123-456-7890</li>
    <li><svg><use href="#icon-phone"/></svg>123-456-7890</li>
    <li><svg><use href="#icon-mail"/></svg>hello@lucidhaven.co.uk</li>
    <li><svg><use href="#icon-web"/></svg>www.lucidhaven.co.uk</li>
  </ul>
  <div class="leaf-art" role="img" aria-label="Faint pink and lilac tree-of-care decoration"></div>
</section>

<section class="sheet env-back">
  <svg class="flap" viewBox="0 0 540 100" preserveAspectRatio="none" aria-hidden="true">
    <path d="M0 0H540V2C532 30 522 42 500 47L290 92Q270 96 250 92L40 47C18 42 8 30 0 2Z" fill="#e9c9f9"/>
  </svg>
  <span class="seal"></span>
</section>

</body>
</html>
```